Book cover design for modern bagpipe music book

This music book will be A4 in size and requires a design for the front and back cover. The focus is on creating a modern and eye catching design, breaking away from the stereotypes of what people think of when they think of bagpipes. Think the OPPOSITE of a bagpiper in a full kilt standing on top of a mountain playing Lanterns on the Moor!

Book title: Wake Stroll Hum Again

Other front cover text : Music for the bagpipes by Dara Colby

Front cover file ideas uploaded

2 pictures of bagpipes attached.

- The real set of bagpipes give an idea of the correct finer details

- The toy bagpipes perhaps have a better shape with the left 'stick' down

Back cover - No real brief. Keen for it not to be a full block single colour though.

Design requires 3mm bleed for print

Open to ideas and suggestions! Thank you!

```html
<!DOCTYPE html>
<html lang="en">
<head>
<meta charset="utf-8">
<title>Wake Stroll Hum Again — Book Cover</title>
<link rel="stylesheet" href="https://fonts.googleapis.com/css2?family=Bebas+Neue&family=Oswald:wght@200&display=swap">
<style>
  :root {
    --cover-black: #0a0906;
    --title-white: #ffffff;
    --art-red: #ea3b2c;
    --art-crimson: #d80a42;
    --art-magenta: #b3104f;
    --art-plum: #7a2c5e;
    --art-teal: #2c6b74;
  }
  html, body {
    margin: 0;
    padding: 0;
    overflow: hidden;
    background: var(--cover-black);
  }
  .cover {
    position: relative;
    width: 848px;
    height: 1200px;
    overflow: hidden;
    background: var(--cover-black);
  }
  .cover__art {
    position: absolute;
    inset: 0;
  }
  .cover__title {
    position: absolute;
    inset: 0;
  }
  .title-line {
    font-family: "Bebas Neue", "Oswald", sans-serif;
    fill: var(--title-white);
  }
  .cover__author {
    position: absolute;
    left: 768px;
    top: 274px;
    margin: 0;
    writing-mode: vertical-rl;
    font-family: "Oswald", sans-serif;
    font-weight: 200;
    font-size: 24px;
    letter-spacing: 14px;
    color: var(--title-white);
    text-transform: uppercase;
    line-height: 1;
  }
</style>
</head>
<body>
  <main class="cover">
    <svg class="cover__art" width="848" height="1200" viewBox="0 0 848 1200"
         role="img" aria-label="Bold silhouette illustration of a set of bagpipes in a red to purple gradient, drones angled diagonally across the cover">
      <defs>
        <linearGradient id="bagpipe-gradient" x1="0.75" y1="0" x2="0.45" y2="1">
          <stop offset="0" stop-color="var(--art-red)"/>
          <stop offset="0.35" stop-color="var(--art-crimson)"/>
          <stop offset="0.6" stop-color="var(--art-magenta)"/>
          <stop offset="0.82" stop-color="var(--art-plum)"/>
          <stop offset="1" stop-color="var(--art-teal)"/>
        </linearGradient>
      </defs>
      <path fill="url(#bagpipe-gradient)"
            d="M760 140 L840 170 L800 250 L650 360 L560 460 L520 560 L640 620 L680 760 L740 820 L700 960 L640 1080 L600 1200 L0 1200 L0 740 L160 560 L210 260 L230 250 L240 430 L330 520 L380 340 L470 250 Z"/>
    </svg>

    <svg class="cover__title" width="848" height="1200" viewBox="0 0 848 1200" aria-label="Wake Stroll Hum Again">
      <text class="title-line" x="6" y="316" font-size="514" textLength="482" lengthAdjust="spacingAndGlyphs">WAKE</text>
      <text class="title-line" x="4" y="568" font-size="343" textLength="604" lengthAdjust="spacingAndGlyphs">STROLL</text>
      <text class="title-line" x="4" y="948" font-size="525" textLength="636" lengthAdjust="spacingAndGlyphs">HUM</text>
      <text class="title-line" x="0" y="1262" font-size="430" textLength="770" lengthAdjust="spacingAndGlyphs">AGAIN</text>
    </svg>

    <p class="cover__author">Author Name</p>
  </main>
</body>
</html>
```